Seven Quiet Steps to Lift the Final Offer on YOUR House - MERVA Real Estate

I have written an E-Book that is called "Seven Quiet Steps to Lift the Final Offer on Your House." The E-Book will be available as a FREE download from my MERVA Real Estate landing page, and also from a Facebook campaign that will be commencing in early September.

The E-Book content is in the WORD document below - I now need for it to be made to look more professional and suitable for publishing and placed on my landing page for download. Please review and send me some proposals for this e-book to be a bit more eye catching and appealing than just a WORD doc.

My MERVA Real Estate landing page is still under development and you can see the what is close to the final proposal here:

http://www.brell-tovan.com.au/merva/

The cover of the E-Book is at the bottom of the page. Please review and give the internals the sale look and feel.

Target Market(s)

Home and Property Owners in the middle ring Eastern Suburbs of Melbourne - approximately 15 - 30 km's from the central business district. The area is a very family oriented area and features mostly houses that are 3 or 4 bedroom - with some larger properties that are five or more bedrooms. The area is quite an expensive suburban community and house prices range between the low of $1,000,000 to a high of more than $2,500,000. The predominant cultural group that buys in this area are Chinese and Chinese Australian buyers. The predominant group who are selling are usually Australians of a white anglo-saxon background. Other groups are of Asian sub continent background (Indian / Sri Lankan/ Pakistan). All are families that are attracted to the area because of the great schools, good shopping, leisure facilities (parks, pools, courts etc), and excellent public and road transport infrastructure. Read the content of my e-book - it tells you every thing you need to know :)

Industry/Entity Type

Real Estate

Colors

Designer to choose colors to be used in the design.

Requirements
Must have
• Once completed the layout should not be too busy - it should be easy to read. I guess then the statement "less is more" is applicable.
• I will probably print a number of copies of this book for distribution as well - so please consider print attributes in the design.
• IMPORTANT: as for any e-book offering specialist advice, the MAIN reason for the book is for the generation of sales leads and to establish the author as a subject matter expert on the topic. Please consider this in your design elements. BUT - the book should also not come across as 1 big advertisement either. Subtle but impactful are well chosen words to describe how it should present.
Nice to have
• MERVA Real Estate branding on every page - to re-inforce the message.
Should not have
• No need for animations or illustrations/

```html
<!DOCTYPE html>
<html lang="en">
<head>
<meta charset="utf-8">
<title>Seven Quiet Steps to Lift the Final Offer on YOUR House - MERVA Real Estate</title>
<link href="https://fonts.googleapis.com/css2?family=Jost:wght@400;500;600;700;800&display=swap" rel="stylesheet">
<style>
  :root {
    --backdrop: #2b2b2d;
    --ink: #0c0c0d;
    --paper: #ffffff;
    --mist-top: #f4f4f7;
    --mist-bottom: #c9c9d1;
    --mint: #6fcfa9;
    --text-dark: #1d1d22;
    --text-soft: #45454d;
    --photo-tone: #d8dade;
  }
  * { box-sizing: border-box; margin: 0; padding: 0; }
  html, body { width: 1200px; height: 789px; overflow: hidden; }
  body {
    background: var(--backdrop);
    font-family: "Jost", "Futura", sans-serif;
    position: relative;
  }
  .spread {
    position: absolute;
    left: 100px; top: 41px;
    width: 1000px; height: 707px;
    display: flex;
    box-shadow: 0 20px 40px rgba(0,0,0,.5);
  }
  .page { position: relative; width: 500px; height: 707px; overflow: hidden; }

  /* Back cover */
  .back-cover { background: linear-gradient(170deg, var(--mist-top) 0%, var(--mist-bottom) 100%); }
  .conclusion { position: absolute; left: 48px; top: 58px; width: 400px; color: var(--text-dark); }
  .conclusion__title {
    font-size: 15px; font-weight: 600; letter-spacing: .5px;
    padding-bottom: 5px; border-bottom: 1px solid var(--text-dark); display: inline-block;
    padding-right: 150px; margin-bottom: 10px;
  }
  .conclusion p { font-size: 8.5px; line-height: 1.45; color: var(--text-soft); margin-bottom: 8px; }
  .conclusion strong { color: var(--text-dark); font-weight: 600; }
  .checklist { list-style: none; margin: 4px 0 12px; }
  .checklist li {
    font-size: 12.5px; font-weight: 500; letter-spacing: .4px; text-transform: uppercase;
    display: flex; align-items: center; gap: 7px; line-height: 1.4;
  }
  .checklist svg { width: 11px; height: 11px; flex: none; }
  .skyline {
    position: absolute; left: 150px; top: 372px; width: 300px; height: 65px;
    background: linear-gradient(180deg, rgba(120,120,130,0) 0%, rgba(120,120,130,.28) 100%);
  }
  .back-cover__band {
    position: absolute; left: 0; right: 0; bottom: 0; height: 270px; background: var(--ink);
  }
  .accent-bar { position: absolute; background: var(--mint); }
  .back-cover .accent-bar--side { left: 0; top: 0; width: 7px; height: 110px; }
  .back-cover .accent-bar--foot { left: 0; bottom: 0; width: 290px; height: 5px; }
  .enquiry { position: absolute; left: 46px; top: 66px; }
  .enquiry__title { color: var(--paper); font-size: 22px; font-weight: 700; letter-spacing: 1px; }
  .enquiry__phone {
    display: flex; align-items: center; gap: 10px; margin-top: 6px;
    color: var(--mint); font-size: 22px; font-weight: 700; letter-spacing: .5px;
  }
  .enquiry__phone svg { width: 21px; height: 21px; }
  .brand { font-weight: 500; letter-spacing: 1px; }
  .back-cover .brand {
    position: absolute; right: 30px; top: 26px; color: var(--paper);
    font-size: 20px; white-space: nowrap;
  }
  .web-address {
    position: absolute; left: 46px; bottom: 38px; color: var(--paper);
    font-size: 15px; font-weight: 500; letter-spacing: .5px;
  }

  /* Front cover */
  .front-cover { background: var(--paper); }
  .front-cover .accent-bar--side { left: 0; top: 0; width: 7px; height: 120px; }
  .front-cover .brand {
    position: absolute; left: 40px; top: 52px; width: 170px;
    color: var(--ink); font-size: 26px; line-height: 1.1;
  }
  .portrait {
    position: absolute; right: 40px; top: 0; width: 230px; height: 400px;
    background: linear-gradient(180deg, var(--photo-tone) 0%, #3a3b40 45%, #1b1b20 100%);
  }
  .front-cover__band {
    position: absolute; left: 0; right: 0; bottom: 0; height: 310px; background: var(--ink);
  }
  .headline {
    position: absolute; left: 50px; top: 60px; width: 420px;
    color: var(--paper); font-size: 33px; font-weight: 400; line-height: 1.12; text-transform: uppercase;
  }
  .headline em { font-style: normal; font-weight: 800; color: var(--mint); }
  .front-cover .accent-bar--foot { right: 0; bottom: 40px; width: 230px; height: 5px; }
</style>
</head>
<body>
  <main class="spread">
    <section class="page back-cover">
      <div class="conclusion">
        <h2 class="conclusion__title">CONCLUSION</h2>
        <p>So when it comes to selling your property anywhere across the City of Monash and the City of Whitehorse it all starts with a solid and proven strategy. Follow the <strong>SEVEN QUIET STEPS TO LIFT THE FINAL OFFER ON YOUR HOUSE!</strong></p>
        <ul class="checklist">
          <li><svg viewBox="0 0 12 12"><path d="M1 6.5 4.5 10 11 2" fill="none" stroke="#1d1d22" stroke-width="2"/></svg>Property Presentation</li>
          <li><svg viewBox="0 0 12 12"><path d="M1 6.5 4.5 10 11 2" fill="none" stroke="#1d1d22" stroke-width="2"/></svg>Pricing</li>
          <li><svg viewBox="0 0 12 12"><path d="M1 6.5 4.5 10 11 2" fill="none" stroke="#1d1d22" stroke-width="2"/></svg>Agent Choice</li>
          <li><svg viewBox="0 0 12 12"><path d="M1 6.5 4.5 10 11 2" fill="none" stroke="#1d1d22" stroke-width="2"/></svg>Marketing and Advertising</li>
          <li><svg viewBox="0 0 12 12"><path d="M1 6.5 4.5 10 11 2" fill="none" stroke="#1d1d22" stroke-width="2"/></svg>Methods of Sale</li>
        </ul>
        <p>I have used this successful strategy time and time again to help my clients achieve top dollar in the sale of their home. At MERVA Real Estate – we are property sales experts.</p>
        <p>Most people buy and sell one or two properties in a lifetime. At MERVA Real Estate – we transact property sales every single week – and we KNOW what works in getting you the best possible price for your home.</p>
        <p>Get us in for a chat and an assessment of your requirements in the sale of your property. I know you won't be disappointed that you did.</p>
      </div>
      <div class="skyline" role="img" aria-label="Line drawing of a city skyline"></div>
      <div class="back-cover__band">
        <span class="accent-bar accent-bar--side"></span>
        <span class="brand">MERVA Real Estate</span>
        <div class="enquiry">
          <h3 class="enquiry__title">GOT QUESTIONS?</h3>
          <div class="enquiry__phone">
            <svg viewBox="0 0 24 24"><circle cx="12" cy="12" r="10.5" fill="none" stroke="#fff" stroke-width="1.5"/><path d="M8.2 6.5c.6-.4 1.3-.2 1.6.4l.9 1.8c.2.5.1 1-.3 1.3l-.8.6c.6 1.4 1.6 2.5 3 3.1l.6-.8c.3-.4.9-.5 1.3-.3l1.8.9c.6.3.8 1 .4 1.6l-.6.9c-.5.7-1.4 1-2.2.7-3.1-1.1-5.4-3.5-6.5-6.5-.3-.8 0-1.7.7-2.2z" fill="#fff"/></svg>
            <span>1800 555 017</span>
          </div>
        </div>
        <p class="web-address">www.brell-tovan.com.au/merva/</p>
        <span class="accent-bar accent-bar--foot"></span>
      </div>
    </section>

    <section class="page front-cover">
      <span class="accent-bar accent-bar--side"></span>
      <span class="brand">MERVA Real Estate</span>
      <div class="portrait" role="img" aria-label="Portrait photo of the agent in a dark suit and striped tie"></div>
      <div class="front-cover__band">
        <h1 class="headline"><em>Seven</em> Quiet <em>Steps</em><br>to <em>Lift</em><br>the <em>Final Offer</em> on<br>YOUR <em>House</em></h1>
        <span class="accent-bar accent-bar--foot"></span>
      </div>
    </section>
  </main>
</body>
</html>
```